Business card design needed

Design:
Want the logo/design to have an enviromental feel
Simple look not to busy

Company Info:
Pre purchase building and pest inspections
Registered building practitoner DB-U 48157 (please include building commission logo in design)

Industry/Entity Type

Building

Contact Information for Business Card

Company name:
Fernway Building and Pest inspections

Inspectors:
Dean Parkes 0471 958 214
Jack Severn 0419 562 847
Email: fernbpi@mailbox-demo.net

```html
<!DOCTYPE html>
<html lang="en">
<head>
<meta charset="utf-8">
<title>Fernway Building and Pest inspections – Business Card</title>
<link href="https://fonts.googleapis.com/css2?family=Bitter:wght@700&family=Fira+Sans:wght@300;400&display=swap" rel="stylesheet">
<style>
  :root {
    --backdrop: #e6e6e6;
    --card: #ffffff;
    --brand-green: #2aa83a;
    --ink: #1c1c1c;
    --navy: #2b2b4a;
  }
  * { margin: 0; padding: 0; box-sizing: border-box; }
  html, body {
    width: 1200px;
    height: 1000px;
    overflow: hidden;
    background: var(--backdrop);
  }
  .card {
    position: absolute;
    left: 100px;
    top: 212px;
    width: 1000px;
    height: 576px;
    background: var(--card);
    overflow: hidden;
  }
  .brand-mark {
    position: absolute;
    left: 82px;
    top: 92px;
    width: 96px;
    height: 96px;
    background: var(--brand-green);
  }
  .company-name {
    position: absolute;
    left: 80px;
    top: 198px;
    font-family: "Bitter", Georgia, serif;
    font-weight: 700;
    font-size: 40px;
    line-height: 56px;
    color: var(--brand-green);
    white-space: nowrap;
  }
  .registration {
    position: absolute;
    right: 82px;
    top: 90px;
    display: flex;
    flex-direction: column;
    align-items: flex-end;
    gap: 2px;
  }
  .registration-badge { display: block; }
  .registration-number {
    font-family: "Fira Sans", Arial, sans-serif;
    font-weight: 400;
    font-size: 13px;
    line-height: 16px;
    letter-spacing: 3px;
    color: var(--navy);
  }
  .contact-name {
    position: absolute;
    left: 82px;
    font-family: "Fira Sans", Arial, sans-serif;
    font-weight: 300;
    font-size: 28px;
    line-height: 34px;
    color: var(--ink);
  }
  .contact-line {
    position: absolute;
    display: flex;
    align-items: center;
    gap: 20px;
    font-family: "Fira Sans", Arial, sans-serif;
    font-weight: 300;
    font-size: 30px;
    line-height: 36px;
    color: var(--ink);
    white-space: nowrap;
  }
  .contact-icon { display: block; flex: none; }
  .name-dean { top: 323px; }
  .phone-dean { left: 81px; top: 370px; }
  .name-jack { top: 430px; }
  .phone-jack { left: 81px; top: 477px; }
  .email-line { right: 82px; top: 477px; }
</style>
</head>
<body>
  <main class="card">
    <div class="brand-mark" aria-hidden="true"></div>
    <h1 class="company-name">Fernway Building and Pest inspections</h1>

    <div class="registration">
      <svg class="registration-badge" width="190" height="58" viewBox="0 0 190 58" role="img" aria-label="Registered building practitioner badge">
        <circle cx="29" cy="29" r="27" fill="none" stroke="var(--navy)" stroke-width="2"/>
        <rect x="70" y="12" width="120" height="34" rx="4" fill="var(--navy)" opacity="0.85"/>
      </svg>
      <span class="registration-number">DB-U 48157</span>
    </div>

    <p class="contact-name name-dean">Dean Parkes</p>
    <p class="contact-line phone-dean">
      <svg class="contact-icon" width="34" height="34" viewBox="0 0 34 34" aria-hidden="true">
        <rect width="34" height="34" rx="7" fill="var(--brand-green)"/>
        <rect x="5" y="5" width="24" height="24" rx="5" fill="#fff"/>
        <path d="M12 9c-2 1-3 3-2 6 1 4 4 8 8 10 2 1 4 0 5-2l-3-3-2 1c-2-1-4-4-5-6l1-2z" fill="var(--brand-green)"/>
      </svg>
      <span>0471 958 214</span>
    </p>

    <p class="contact-name name-jack">Jack Severn</p>
    <p class="contact-line phone-jack">
      <svg class="contact-icon" width="34" height="34" viewBox="0 0 34 34" aria-hidden="true">
        <rect width="34" height="34" rx="7" fill="var(--brand-green)"/>
        <rect x="5" y="5" width="24" height="24" rx="5" fill="#fff"/>
        <path d="M12 9c-2 1-3 3-2 6 1 4 4 8 8 10 2 1 4 0 5-2l-3-3-2 1c-2-1-4-4-5-6l1-2z" fill="var(--brand-green)"/>
      </svg>
      <span>0419 562 847</span>
    </p>

    <p class="contact-line email-line">
      <svg class="contact-icon" width="34" height="34" viewBox="0 0 34 34" aria-hidden="true">
        <rect width="34" height="34" rx="7" fill="var(--brand-green)"/>
        <rect x="7" y="10" width="20" height="14" rx="1.5" fill="#fff"/>
        <path d="M7.5 11l9.5 7.5 9.5-7.5" fill="none" stroke="var(--brand-green)" stroke-width="2"/>
      </svg>
      <span>fernbpi@mailbox-demo.net</span>
    </p>
  </main>
</body>
</html>
```